Webshop for furniture and lamps

We need a design for a web shop with APP that should have two options:
1-Webshop in general which should attract to private customer in general and
2-Website that is meant to attract big customers as hotels and restaurants who would have their own customerize login.

That's the idea behind the shop.

It should be diveded into 4 parts
vintage furniture
rattan set outdoor and indoor
lamps and
wooden wall decor

The name of the shop is borgo veneria!

Please kindly make me an offer.

Reason: Dear designers, so far there hasn't been a design that really matched. Look up German web sites like www.trevolind.de or www.quandor17.de... Haven't been convinced by designs! Sorry folks. Please submit some new ones. Kind regards Tam

```html
<!DOCTYPE html>
<html lang="en">
<head>
<meta charset="utf-8">
<title>Borgo Veneria – Furniture &amp; Lamps</title>
<link rel="stylesheet" href="https://fonts.googleapis.com/css2?family=Yanone+Kaffeesatz:wght@400;600;700&family=Signika:wght@400;600;700&family=Questrial&display=swap">
<style>
  :root {
    --brown: #a08456;
    --brown-dark: #8c7352;
    --floor: #c99463;
    --floor-soft: #d4a06e;
    --panel: #ffffff;
    --ink: #111111;
    --ink-soft: #444444;
    --yellow: #f6cf68;
    --link-green: #2f8f7f;
    --line: #9a9a9a;
  }
  * { margin: 0; padding: 0; box-sizing: border-box; }
  html, body { width: 699px; height: 1200px; overflow: hidden; background: #fff; }
  body { position: relative; font-family: "Questrial", sans-serif; color: var(--ink); }
  .abs { position: absolute; }

  .floor-backdrop {
    position: absolute; left: 0; top: 62px; width: 699px; height: 1138px;
    background: linear-gradient(180deg, var(--floor-soft), var(--floor));
  }

  /* header */
  .site-header { position: absolute; left: 0; top: 0; width: 699px; height: 62px; background: #fff; }
  .brand-box {
    position: absolute; left: 68px; top: 0; width: 138px; height: 73px; background: var(--brown);
    display: flex; align-items: flex-end; justify-content: center; padding-bottom: 14px;
    font-family: "Signika", sans-serif; font-weight: 600; font-size: 19px; color: #fff; z-index: 3;
  }
  .account-link { left: 491px; top: 5px; font-size: 8px; color: var(--brown); }
  .cart-button {
    left: 544px; top: 0; width: 58px; height: 18px; background: var(--brown); color: #fff;
    font-size: 7.5px; display: flex; align-items: center; justify-content: center; gap: 4px;
  }
  .search-button { left: 608px; top: 0; width: 23px; height: 18px; background: var(--brown); }
  .main-nav {
    left: 247px; top: 45px; width: 385px; display: flex; justify-content: space-between;
    font-family: "Signika", sans-serif; font-weight: 600; font-size: 7.4px; color: var(--brown); letter-spacing: .2px;
  }
  .main-nav span.sep { font-weight: 400; }

  .panel { position: absolute; background: var(--panel); border-radius: 14px; }

  /* hero */
  .hero { left: 70px; top: 79px; width: 562px; height: 309px; overflow: hidden; }
  .made-in { right: 32px; top: 35px; font-family: "Yanone Kaffeesatz", sans-serif; font-weight: 600; font-size: 10px; color: var(--brown); display: flex; align-items: center; gap: 4px; }
  .flag-mark { width: 15px; height: 10px; background: #2d3f8f; }
  .hero-title {
    left: 0; top: 68px; width: 562px; text-align: center;
    font-family: "Yanone Kaffeesatz", sans-serif; font-weight: 700; font-size: 54px; line-height: 1; color: var(--brown);
  }
  .hero-photo {
    left: 0; top: 145px; width: 562px; height: 164px;
    background: linear-gradient(180deg, #f3f1ec 0%, #b5a58b 35%, #6f5c44 70%, #8a7a66 100%);
  }
  .hero-caption {
    left: 57px; top: 162px; width: 243px; padding: 3px 6px;
    background: rgba(40,32,22,.55); color: #fff;
    font-family: "Signika", sans-serif; font-weight: 600; font-size: 11px; line-height: 15px;
  }
  .btn-yellow {
    left: 68px; top: 211px; width: 58px; height: 18px; background: var(--yellow); color: #3a2d16;
    font-family: "Yanone Kaffeesatz", sans-serif; font-weight: 600; font-size: 12px;
    display: flex; align-items: center; justify-content: center;
  }
  .slider-arrow { top: 143px; width: 24px; height: 24px; border-radius: 50%; border: 1.5px solid rgba(246,207,104,.8); }
  .slider-dots { left: 282px; top: 276px; display: flex; gap: 2px; }
  .slider-dots i { width: 7px; height: 7px; border-radius: 50%; border: 1.5px solid #fff; display: block; }

  /* welcome */
  .welcome { left: 68px; top: 411px; width: 343px; height: 180px; }
  .section-heading { font-family: "Signika", sans-serif; font-weight: 400; color: var(--brown); }
  .welcome h2 { position: absolute; left: 19px; top: 14px; font-size: 17px; }
  .welcome p { position: absolute; left: 14px; top: 41px; width: 306px; font-size: 7.5px; line-height: 12px; font-weight: 700; }
  .btn-brown {
    background: var(--brown); color: #fff; font-family: "Yanone Kaffeesatz", sans-serif; font-weight: 600;
    display: flex; align-items: center; justify-content: center;
  }
  .welcome .btn-brown { left: 129px; top: 154px; width: 58px; height: 18px; font-size: 12px; }

  /* testimonial */
  .testimonial { left: 424px; top: 411px; width: 207px; height: 180px; }
  .quote-mark { font-family: "Signika", sans-serif; font-weight: 700; font-size: 28px; color: #d6d0c4; line-height: 1; }
  .testimonial .quote-text { position: absolute; left: 22px; top: 29px; width: 163px; font-size: 7.2px; line-height: 12px; color: var(--ink-soft); }
  .testimonial .author { left: 98px; top: 131px; font-family: "Signika", sans-serif; font-weight: 600; font-size: 10px; color: var(--brown); }
  .testimonial .all-link { left: 0; top: 168px; width: 207px; text-align: center; font-size: 6.5px; color: var(--brown); text-decoration: underline; }

  /* products */
  .products { left: 70px; top: 610px; width: 562px; height: 379px; }
  .products h2 { position: absolute; left: 16px; top: 11px; font-size: 11px; font-weight: 600; }
  .products .range-link { right: 18px; top: 16px; font-size: 5.8px; color: var(--brown); }
  .products .intro { left: 14px; top: 27px; font-size: 7px; font-weight: 700; white-space: nowrap; }
  .product-card {
    position: absolute; top: 51px; width: 121px; height: 310px;
    border: 1px solid var(--line); border-radius: 4px; background: #fff; overflow: hidden;
  }
  .product-card h3 {
    position: absolute; left: 13px; top: 14px; width: 104px;
    font-family: "Signika", sans-serif; font-weight: 600; font-size: 16.5px; line-height: 19px; color: var(--ink);
  }
  .product-card h3 em { font-style: normal; color: var(--brown); }
  .product-card .product-photo { position: absolute; left: 0; top: 73px; width: 121px; height: 120px; }
  .product-card p { position: absolute; left: 6px; top: 209px; width: 109px; text-align: center; font-size: 8.6px; line-height: 12.5px; font-weight: 700; }
  .product-card .btn-brown { position: absolute; left: 31px; top: 265px; width: 59px; height: 19px; font-size: 12px; }

  /* subscribe */
  .subscribe-band { left: 70px; top: 1008px; width: 562px; height: 102px; }
  .subscribe-box { left: 16px; top: 23px; width: 263px; height: 59px; background: var(--brown-dark); }
  .subscribe-box .stitch { position: absolute; inset: 3px; border: 1px dashed rgba(255,255,255,.55); }
  .subscribe-box h4 { position: absolute; left: 0; top: 6px; width: 263px; text-align: center; font-family: "Signika", sans-serif; font-weight: 600; font-size: 13px; color: #fff; }
  .email-field {
    position: absolute; left: 15px; top: 24px; width: 229px; height: 26px; background: #fff; border-radius: 3px;
    font-size: 8.5px; color: #9a9a9a; display: flex; align-items: center; padding-left: 10px;
  }
  .email-go { position: absolute; right: 4px; top: 4px; width: 19px; height: 18px; background: var(--brown); border-radius: 2px; }
  .tweet-bubble { left: 301px; top: 22px; width: 209px; height: 61px; border: 1.5px solid #c9c9c9; border-radius: 12px; background: #fff; }
  .tweet { position: absolute; top: 6px; width: 92px; font-size: 5.6px; line-height: 7.2px; color: var(--ink-soft); }
  .tweet a { color: var(--link-green); text-decoration: none; }
  .tweet time { display: block; margin-top: 5px; padding-left: 34px; font-style: italic; }
  .social-round { width: 22px; height: 22px; border-radius: 50%; border: 1.5px solid #d2d2d2; background: #fff; display: flex; align-items: center; justify-content: center; }
  .social-round i { width: 12px; height: 12px; border-radius: 50%; background: #57a8d8; display: block; }

  .footer-name { left: 0; top: 1116px; width: 699px; text-align: center; font-family: "Signika", sans-serif; font-weight: 700; font-size: 22px; color: var(--ink); }

  .site-footer { left: 70px; top: 1153px; width: 562px; height: 60px; }
  .site-footer .rule { position: absolute; left: 14px; top: 14px; width: 532px; height: 1px; background: #d8d8d8; }
  .footer-links { left: 28px; top: 24px; display: flex; gap: 9px; font-size: 6.5px; font-weight: 700; }
  .footer-follow { left: 448px; top: 21px; display: flex; align-items: center; gap: 4px; font-size: 6.5px; font-weight: 700; }
  .footer-follow i { width: 14px; height: 14px; border-radius: 50%; display: block; }
</style>
</head>
<body>

<div class="floor-backdrop" role="img" aria-label="Photo of warm oak plank flooring as page background"></div>

<header class="site-header">
  <div class="brand-box">Borgo Veneria</div>
  <a class="abs account-link">My Account</a>
  <div class="abs cart-button">My Cart
    <svg width="10" height="8" viewBox="0 0 10 8"><path d="M0 1h2l1 5h6l1-4H3" fill="none" stroke="#fff" stroke-width="1"/></svg>
  </div>
  <div class="abs search-button">
    <svg width="23" height="18" viewBox="0 0 23 18"><circle cx="10.5" cy="8" r="4.5" fill="none" stroke="#fff" stroke-width="1.6"/><path d="M13.8 11.2l3.5 3.5" stroke="#fff" stroke-width="1.8"/></svg>
  </div>
  <nav class="abs main-nav">
    <span>VINTAGE FURNITURE</span><span class="sep">|</span>
    <span>RATTAN SET OUTDOOR AND INDOOR</span><span class="sep">|</span>
    <span>LAMPS</span><span class="sep">|</span>
    <span>WOODEN WALL DECOR</span>
  </nav>
</header>

<section class="panel hero">
  <div class="abs made-in">Made in <span class="flag-mark"></span> Australia</div>
  <h1 class="abs hero-title">A NEW LEVEL OF FURNITURE</h1>
  <div class="abs hero-photo" role="img" aria-label="Wicker rattan sofa, armchair and round table on a sunny wooden deck"></div>
  <div class="abs hero-caption">We know that you will not Buy the Furniture which one you don't Like...</div>
  <div class="abs btn-yellow">LEARN MORE</div>
  <div class="abs slider-arrow" style="left:16px"></div>
  <div class="abs slider-arrow" style="left:530px"></div>
  <div class="abs slider-dots"><i></i><i></i><i></i><i></i></div>
</section>

<section class="panel welcome">
  <h2 class="section-heading">Welcome to our website</h2>
  <p>Lorem Ipsum is simply dummy text of the printing and typesetting industry. Lorem Ipsum has been the industry's standard dummy text ever since the 1500s, when an unknown printer took a galley of type and scrambled it to make a type specimen book. It has survived not only five centuries, but also the leap into electronic typesetting, remaining essentially unchange Lorem Ipsum is simply dummy text of the printing and typesetting industry. Lorem Ips um has been the industry's standard dummy text ever since the 1500s, Lorem Ipsum is simply dummy text of the printing and typesetting industry. Lorem Ipsum has been the industry's Lorem Ipsum is simply dummy text of the printing and typesetting industry.</p>
  <div class="abs btn-brown">LEARN MORE</div>
</section>

<aside class="panel testimonial">
  <div class="abs quote-mark" style="left:22px;top:8px">&ldquo;</div>
  <p class="quote-text">Lorem Ipsum is simply dummy text of the printing and typesetting industry. Lorem Ipsum has been the industry's standard dummy text ever since the 1500s, when an unknown printer took a galley of type and scrambled it to make a type specimen book. It has survived not only five centuries, but also the leap into electronic typesetting, remaining essentially unchanged.</p>
  <div class="abs quote-mark" style="left:74px;top:125px">&rdquo;</div>
  <div class="abs author">Name O' here</div>
  <a class="abs all-link">view all testimonials</a>
</aside>

<section class="panel products">
  <h2 class="section-heading">Our Products</h2>
  <a class="abs range-link">view our full product range &gt;&gt;</a>
  <p class="abs intro">Lorem Ipsum is simply dummy text of the printing and typesetting industry. Lorem Ipsum has been the industry's standard dummy text ever since the 1500s,</p>

  <article class="product-card" style="left:13px">
    <h3>Vintage <em>Furniture</em></h3>
    <div class="product-photo" role="img" aria-label="Dark wooden vintage cabinet with painted tile drawers" style="background:linear-gradient(135deg,#efe9e2,#6b4a33 45%,#4a3222 70%,#c9b9a8)"></div>
    <p>Lorem Ipsum is simply dummy text of the printing and typesetting industry.</p>
    <div class="btn-brown">View All</div>
  </article>

  <article class="product-card" style="left:149px">
    <h3>Rattan Set <em>Outdoor</em> and Indoor</h3>
    <div class="product-photo" role="img" aria-label="Black rattan chairs around a glass table on a timber deck" style="background:linear-gradient(180deg,#8a6a4e,#3a3a3a 45%,#2a2a2a 70%,#7a5e48)"></div>
    <p>Lorem Ipsum is simply dummy text of the printing and typesetting industry.</p>
    <div class="btn-brown">View All</div>
  </article>

  <article class="product-card" style="left:285px">
    <h3>Beautiful <em>Lamps</em></h3>
    <div class="product-photo" role="img" aria-label="Floor lamp with striped black and gold shade" style="background:linear-gradient(180deg,#f2f2f2,#e6e4e0 50%,#f4f4f4)"></div>
    <p>Lorem Ipsum is simply dummy text of the printing and typesetting industry.</p>
    <div class="btn-brown">View All</div>
  </article>

  <article class="product-card" style="left:420px">
    <h3>Wooden Wall <em>Decor</em></h3>
    <div class="product-photo" role="img" aria-label="Textured wooden wall panel made of small timber blocks" style="background:linear-gradient(135deg,#5e4330,#8a6a4c 50%,#c8b8a4)"></div>
    <p>Lorem Ipsum is simply dummy text of the printing and typesetting industry.</p>
    <div class="btn-brown">View All</div>
  </article>
</section>

<section class="panel subscribe-band">
  <div class="abs subscribe-box">
    <div class="stitch"></div>
    <h4>Subcribe to the borgo veneria Shop</h4>
    <div class="email-field">Please Enter your email address
      <span class="email-go">
        <svg width="19" height="18" viewBox="0 0 19 18"><path d="M8 5l4 4-4 4" fill="none" stroke="#fff" stroke-width="1.8"/></svg>
      </span>
    </div>
  </div>
  <div class="abs tweet-bubble">
    <div class="tweet" style="left:8px">Lorem Ipsum is simply dummy text of the printing and typese tting industry. Lorem Ipsum has been the. <a>http://veneria-news.de/post</a><time>1st jan, 12:00pm</time></div>
    <div class="tweet" style="left:106px">Lorem Ipsum is simply dummy text of the printing and typese tting industry. Lorem Ipsum has been the. <a>http://veneria-news.de/post</a><time>1st jan, 12:00pm</time></div>
  </div>
  <div class="abs social-round" style="left:521px;top:41px"><i></i></div>
</section>

<div class="abs footer-name">Borgo Veneria</div>

<footer class="panel site-footer">
  <div class="rule"></div>
  <nav class="abs footer-links">
    <span>About Us</span><span>|</span><span>Contact Us</span><span>|</span><span>Privacy Policy</span><span>|</span><span>Terms &amp; Conditions</span><span>|</span><span>Site Map</span>
  </nav>
  <div class="abs footer-follow">Follow Us:
    <i style="background:#3b5b9a"></i><i style="background:#3aa0dc"></i><i style="background:#d9302c"></i>
  </div>
</footer>

</body>
</html>
```